HALVORSEN Business Cards & Stationary
Business Cards & Stationary
HALVORSEN Business Cards & Stationary -
Creative Brief
Modern
Marcus Halvorsen
President
718 North Cobb Parkway Suite 260 Warrenton, VA 20394
855-ASK-HALV
mhalvorsen@halvorsengrp.com
www.halvorsengrp.com
DO NOT USE LOGO FROM WEBSITE. Recent logo done under project HALVORSEN.
LOGO? Not decided if second side is needed, designer to decide.

```html
<!DOCTYPE html>
<html lang="en">
<head>
<meta charset="utf-8">
<title>HALVORSEN Business Cards &amp; Stationery</title>
<link href="https://fonts.googleapis.com/css2?family=Lato:wght@400;700&display=swap" rel="stylesheet">
<style>
  :root {
    --backdrop: #7a7b7d;
    --paper: #ffffff;
    --brand-blue: #2e6485;
    --ink: #5b6670;
    --faint: #eeefef;
    --shadow: rgba(0,0,0,0.28);
  }
  * { margin: 0; padding: 0; box-sizing: border-box; }
  html, body { width: 1200px; height: 893px; overflow: hidden; }
  body {
    position: relative;
    background: var(--backdrop);
    font-family: "Lato", sans-serif;
    color: var(--ink);
  }
  .sheet {
    position: absolute;
    background: var(--paper);
    box-shadow: 2px 3px 8px var(--shadow);
    overflow: hidden;
  }
  .brand {
    display: flex;
    flex-direction: column;
    align-items: center;
    gap: 6px;
  }
  .brand-square { background: var(--brand-blue); }
  .brand-name {
    font-family: "Lato", sans-serif;
    font-weight: 400;
    color: var(--brand-blue);
    letter-spacing: 0.14em;
    white-space: nowrap;
  }
  .faint-mark {
    position: absolute;
    background: var(--faint);
  }

  /* Letterhead */
  .letterhead { left: 53px; top: 121px; width: 518px; height: 748px; }
  .letterhead .brand { position: absolute; left: 0; right: 0; top: 60px; }
  .letterhead .brand-square { width: 40px; height: 40px; }
  .letterhead .brand-name { font-size: 12px; }
  .letterhead .faint-mark { left: 177px; top: 314px; width: 278px; height: 300px; }
  .letterhead-web {
    position: absolute; left: 0; right: 0; top: 640px;
    text-align: center; font-size: 10px; font-weight: 700;
    color: var(--brand-blue); letter-spacing: 0.04em;
  }
  .letterhead-rule {
    position: absolute; left: 140px; right: 140px; top: 658px;
    height: 1px; background: var(--brand-blue);
  }
  .letterhead-footer {
    position: absolute; left: 18px; right: 18px; top: 730px;
    display: flex; justify-content: space-between;
    font-size: 6px; color: var(--ink); white-space: nowrap;
  }

  /* Business card front */
  .card-front { left: 612px; top: 128px; width: 235px; height: 119px; }
  .card-front .brand { position: absolute; left: 20px; top: 14px; align-items: flex-start; gap: 4px; }
  .card-front .brand-square { width: 24px; height: 24px; }
  .card-front .brand-name { font-size: 7px; }
  .card-front .faint-mark { left: 175px; top: 14px; width: 60px; height: 95px; }
  .card-contact { position: absolute; left: 20px; top: 62px; font-size: 5px; line-height: 1.6; white-space: nowrap; }
  .card-person { font-weight: 700; color: var(--brand-blue); font-size: 6px; letter-spacing: 0.06em; }

  /* Business card back */
  .card-back { left: 859px; top: 128px; width: 276px; height: 119px; background: var(--brand-blue); }
  .card-back-web { position: absolute; left: 150px; top: 88px; font-size: 6px; color: var(--paper); white-space: nowrap; }
  .card-back-square { position: absolute; left: 243px; top: 84px; width: 14px; height: 14px; background: var(--paper); }

  /* Envelope back */
  .envelope-back { left: 576px; top: 273px; width: 588px; height: 240px; }
  .envelope-flap { position: absolute; left: 0; top: 0; }
  .envelope-back .brand { position: absolute; left: 0; right: 0; top: 32px; gap: 6px; }
  .envelope-back .brand-square { width: 22px; height: 22px; background: var(--paper); }
  .envelope-back-web { font-size: 6.5px; color: var(--paper); letter-spacing: 0.04em; white-space: nowrap; }

  /* Envelope front */
  .envelope-front { left: 576px; top: 554px; width: 588px; height: 270px; }
  .envelope-front .brand { position: absolute; left: 48px; top: 35px; align-items: flex-start; gap: 4px; }
  .envelope-front .brand-square { width: 28px; height: 28px; }
  .envelope-front .brand-name { font-size: 7.5px; }
  .envelope-front .faint-mark { left: 370px; top: 60px; width: 200px; height: 190px; }
  .return-address { position: absolute; left: 48px; top: 100px; font-size: 5px; line-height: 1.6; white-space: nowrap; }
</style>
</head>
<body>

  <section class="sheet letterhead">
    <div class="faint-mark" role="img" aria-label="Large faint brand initial watermark"></div>
    <div class="brand">
      <div class="brand-square"></div>
      <div class="brand-name">HALVORSEN</div>
    </div>
    <div class="letterhead-web">www.halvorsengrp.com</div>
    <div class="letterhead-rule"></div>
    <div class="letterhead-footer">
      <span>718 Larkspur Avenue Suite 260 Warrenton, VA 20394</span>
      <span>Tel 855-ASK-HALV</span>
      <span>mhalvorsen@halvorsengrp.com</span>
    </div>
  </section>

  <section class="sheet card-front">
    <div class="faint-mark" role="img" aria-label="Faint brand initial watermark"></div>
    <div class="brand">
      <div class="brand-square"></div>
      <div class="brand-name">HALVORSEN</div>
    </div>
    <div class="card-contact">
      <div class="card-person">MARCUS HALVORSEN</div>
      <div>President</div>
      <div>718 Larkspur Avenue Suite 260 Warrenton, VA 20394</div>
      <div>Tel 855-ASK-HALV &nbsp; mhalvorsen@halvorsengrp.com</div>
    </div>
  </section>

  <section class="sheet card-back">
    <div class="card-back-web">www.halvorsengrp.com</div>
    <div class="card-back-square"></div>
  </section>

  <section class="sheet envelope-back">
    <svg class="envelope-flap" width="588" height="240" viewBox="0 0 588 240">
      <polygon points="0,0 588,0 588,42 294,92 0,42" fill="#2e6485"/>
    </svg>
    <div class="brand">
      <div class="brand-square"></div>
      <div class="envelope-back-web">www.halvorsengrp.com</div>
    </div>
  </section>

  <section class="sheet envelope-front">
    <div class="faint-mark" role="img" aria-label="Faint brand initial watermark"></div>
    <div class="brand">
      <div class="brand-square"></div>
      <div class="brand-name">HALVORSEN</div>
    </div>
    <div class="return-address">
      <div>718 Larkspur Avenue Suite 260 Warrenton, VA 20394</div>
      <div>www.halvorsengrp.com</div>
    </div>
  </section>

</body>
</html>
```